SipLoop Business Cards

Hi designers!

Here's some background on our start-up and this project:

SipLoop is a website that will allow users to order alcohol from nearby liquor stores and have it delivered to their homes in minutes. We are really excited to work on creating the best online, alcohol purchasing experience for the users.

So why SipLoop? We like to think of ourselves as that great friend who will get alcohol for you because he happens to have a car. We help you drink in with your friends, family, or guests. Our site will target students and young professionals (of drinking age) who are comfortable buying things online or through apps. We don't see this service as a luxury, VIP, or niche service in the least; instead, we think of us as a relaxed, service-driven start-up that believes in simple design and transparent .

Now, we want a business card that incorporates our newly acquired logo design and some complimenting colors and fonts. Feel free to do it single or double sided, although I'm a sucker for double...

If you happen to have any questions, want to throw some ideas around, or just want some feedback- email me at marco@siploop.example.

Marco Tessin
Founder

Industry/Entity Type

Business

Requirements
Must have
• Name, Position, Email, Cell-phone

No address, no fax, no land-line.

```html
<!DOCTYPE html>
<html lang="en">
<head>
<meta charset="utf-8">
<title>SipLoop Business Cards</title>
<link rel="stylesheet" href="https://fonts.googleapis.com/css2?family=Montserrat:wght@400;600;700;800&display=swap">
<style>
  :root {
    --backdrop: #2a2a2a;
    --card-white: #f7f7f7;
    --brand-yellow: #e6b21f;
    --ink: #1d1d1d;
    --ink-soft: #555555;
    --label-yellow: #e0a91a;
  }
  * { box-sizing: border-box; margin: 0; padding: 0; }
  html, body {
    width: 1200px;
    height: 901px;
    overflow: hidden;
    background: var(--backdrop);
    font-family: "Montserrat", sans-serif;
  }
  .card {
    position: absolute;
    left: 280px;
    width: 640px;
    height: 366px;
    overflow: hidden;
    box-shadow: 0 12px 30px rgba(0, 0, 0, 0.45);
  }
  .card-front {
    top: 60px;
    background: var(--card-white);
    color: var(--ink);
  }
  .card-back {
    top: 470px;
    background: var(--brand-yellow);
  }
  .brand-name {
    position: absolute;
    left: 46px;
    top: 92px;
    font-weight: 800;
    font-size: 50px;
    letter-spacing: -1px;
    color: var(--ink);
  }
  .brand-site {
    position: absolute;
    left: 48px;
    top: 156px;
    font-weight: 700;
    font-size: 12px;
    color: var(--ink);
  }
  .contact-list {
    position: absolute;
    right: 44px;
    top: 100px;
    list-style: none;
    font-size: 14px;
    line-height: 1.35;
  }
  .contact-list .label {
    display: inline-block;
    width: 48px;
    font-weight: 700;
    color: var(--label-yellow);
  }
  .contact-list .value { color: var(--ink-soft); }
  .person {
    position: absolute;
    left: 48px;
    bottom: 56px;
  }
  .person-name {
    font-weight: 700;
    font-size: 16px;
    color: var(--ink);
  }
  .person-role {
    font-size: 16px;
    color: var(--ink-soft);
  }
  .back-wordmark {
    position: absolute;
    left: 18px;
    bottom: -42px;
    font-weight: 800;
    font-size: 196px;
    letter-spacing: -8px;
    line-height: 1;
    color: var(--ink);
    white-space: nowrap;
  }
</style>
</head>
<body>
  <section class="card card-front">
    <div class="brand-name">SipLoop</div>
    <div class="brand-site">www.siploop.example</div>
    <ul class="contact-list">
      <li><span class="label">cell</span><span class="value">555 010 0199</span></li>
      <li><span class="label">email</span><span class="value">marco@siploop.example</span></li>
    </ul>
    <div class="person">
      <div class="person-name">Marco Tessin</div>
      <div class="person-role">Founder</div>
    </div>
  </section>

  <section class="card card-back">
    <div class="back-wordmark">SipLoop</div>
  </section>
</body>
</html>
```